Bref créative
Dale's Furniture
Stationary, Letterhead, Business Cards, Envelopes
I need single sided standard sized Business Card [3.5" x 2"]
Similar to Logo Font
Bright & Fun-filled
Dale's Furniture and Appliances
4817 W. Corvel Ave.
Chicago IL 60688
Dalesfurnitureandappliances@quillmail.example
www.dalesfurnitureandapplianes.example
Current Logo
Black and White Version

```html
<!DOCTYPE html>
<html lang="en">
<head>
<meta charset="utf-8">
<title>Dale's Furniture — Business Card</title>
<link href="https://fonts.googleapis.com/css2?family=Cinzel:wght@700&family=Tinos:wght@400&display=swap" rel="stylesheet">
<style>
  :root {
    --backdrop: #e9e6e2;
    --card: #ffffff;
    --brand-red: #e3141b;
    --deep-red: #b30b10;
    --ink: #1c1c1c;
    --rule: #c9161c;
    --stripe-black: #161616;
    --stripe-grey: #9a9a9a;
  }
  html, body {
    margin: 0;
    width: 1200px;
    height: 756px;
    overflow: hidden;
    background: var(--backdrop);
  }
  .card {
    position: absolute;
    left: 40px;
    top: 58px;
    width: 1120px;
    height: 640px;
    background: var(--card);
    overflow: hidden;
    box-shadow: 0 4px 18px rgba(0,0,0,0.18);
    font-family: "Tinos", "Times New Roman", serif;
    color: var(--ink);
  }
  .brand-square {
    position: absolute;
    left: 206px;
    top: 34px;
    width: 64px;
    height: 64px;
    background: var(--brand-red);
  }
  .brand-name {
    position: absolute;
    left: 66px;
    top: 132px;
    margin: 0;
    font-family: "Cinzel", Georgia, serif;
    font-weight: 700;
    font-size: 42px;
    letter-spacing: 0.5px;
    color: var(--ink);
    white-space: nowrap;
  }
  .tagline {
    position: absolute;
    left: 68px;
    top: 196px;
    width: 366px;
    border-top: 2px solid var(--rule);
    border-bottom: 2px solid var(--rule);
    padding: 2px 0 1px;
    font-family: "Cinzel", Georgia, serif;
    font-weight: 700;
    font-size: 17px;
    text-align: center;
    color: var(--ink);
    white-space: nowrap;
  }
  .since {
    position: absolute;
    left: 68px;
    top: 232px;
    width: 366px;
    text-align: center;
    font-family: "Cinzel", Georgia, serif;
    font-weight: 700;
    font-size: 17px;
    color: var(--brand-red);
  }
  .contact {
    position: absolute;
    left: 82px;
    font-size: 28px;
    line-height: 38px;
    display: flex;
    align-items: flex-start;
    gap: 14px;
    white-space: nowrap;
  }
  .contact svg { flex: none; margin-top: 8px; }
  .contact-address { top: 272px; }
  .contact-phone { top: 376px; }
  .contact-fax { top: 414px; }
  .contact-email { top: 452px; }
  .swoosh {
    position: absolute;
    left: 0;
    top: 0;
  }
  .website {
    position: absolute;
    right: 56px;
    top: 588px;
    font-size: 24px;
    color: #ffffff;
    white-space: nowrap;
  }
</style>
</head>
<body>
  <main class="card">
    <div class="brand-square"></div>
    <h1 class="brand-name">Dale's Furniture</h1>
    <div class="tagline">Appliances And Home Furnishings</div>
    <div class="since">Since 1975</div>

    <svg class="swoosh" width="1120" height="640" viewBox="0 0 1120 640" aria-hidden="true">
      <defs>
        <linearGradient id="redFlow" x1="0" y1="0" x2="1" y2="0">
          <stop offset="0" stop-color="var(--deep-red)"/>
          <stop offset="0.5" stop-color="var(--brand-red)"/>
          <stop offset="1" stop-color="var(--deep-red)"/>
        </linearGradient>
      </defs>
      <path d="M0 640 L0 602 C 380 612, 800 565, 1120 412 L1120 640 Z" fill="url(#redFlow)"/>
      <path d="M0 614 C 380 624, 800 580, 1120 444 L1120 458 C 800 596, 380 640, 0 630 Z" fill="var(--stripe-black)"/>
      <path d="M0 592 C 380 602, 800 554, 1120 400" fill="none" stroke="var(--stripe-grey)" stroke-width="3"/>
      <path d="M0 582 C 380 592, 800 544, 1120 390" fill="none" stroke="var(--brand-red)" stroke-width="2"/>
      <path d="M0 640 L0 636 C 380 646, 800 604, 1120 474 L1120 484 C 800 616, 380 652, 0 640 Z" fill="#ffffff" opacity="0.35"/>
    </svg>

    <div class="contact contact-address">
      <svg width="24" height="18" viewBox="0 0 24 18" aria-hidden="true">
        <rect x="1" y="1" width="22" height="16" rx="2" fill="none" stroke="var(--brand-red)" stroke-width="2"/>
        <path d="M2 2 L12 10 L22 2" fill="none" stroke="var(--brand-red)" stroke-width="2"/>
      </svg>
      <div>4817 W. Corvel Ave.<br>Chicago IL 60688</div>
    </div>

    <div class="contact contact-phone">
      <svg width="22" height="22" viewBox="0 0 22 22" aria-hidden="true">
        <circle cx="11" cy="11" r="10" fill="none" stroke="var(--brand-red)" stroke-width="2"/>
        <path d="M8 6 L10 6 L10.5 9 L9.3 10 Q10.5 12.8 12.5 13.5 L13.5 12.3 L16 13 L16 15 Q11 16 7.5 11 Q6.5 8 8 6 Z" fill="var(--brand-red)"/>
      </svg>
      <div>773-555-0142</div>
    </div>

    <div class="contact contact-fax">
      <svg width="22" height="22" viewBox="0 0 22 22" aria-hidden="true">
        <rect x="5" y="2" width="12" height="6" fill="none" stroke="var(--brand-red)" stroke-width="2"/>
        <rect x="2" y="8" width="18" height="10" rx="2" fill="var(--brand-red)"/>
        <rect x="6" y="14" width="10" height="6" fill="#fff" stroke="var(--brand-red)" stroke-width="1.5"/>
      </svg>
      <div>773-555-0187</div>
    </div>

    <div class="contact contact-email">
      <svg width="22" height="22" viewBox="0 0 22 22" aria-hidden="true">
        <text x="11" y="17" text-anchor="middle" font-family="Tinos, serif" font-size="19" fill="var(--brand-red)">@</text>
      </svg>
      <div>Dalesfurnitureandappliances@quillmail.example</div>
    </div>

    <div class="website">www.dalesfurnitureandapplianes.example</div>
  </main>
</body>
</html>
```